High Profile Web Design Project

We need a sleek,state-of-the-art design for an international real estate company based in the Gulf region.

Fonts should be modern and clean, and a corner should in the top banner should be reserved for the logo.

The logo of the company is gold, navy blue, and white so the website should coincide with this.

The site will actually be an internal portal so it is important that the focus is on content.

This is the first of many requests. Top ten designers will be contacted repeatedly both via the site and privately for further business.

As this is an internal portal for employees, focus should be on news, policies, search, complaints, etc.
Updates

Hi All, 

More information on the requirements: 

1- Group Homepage (Do not include department  component like : Department News, Department Blog, Poll, Calendar)

·         Company Announcements

·         Qalvor in Press

·         Highlights / Achievements (Three main blocks with photos )

·         Photo Gallery

·         Quick Links (Trelvix – Pendrum – Organization Structure – Phone Directory …)

·         Navigation tabs
- Properties (Include sub links for departments)
-International (Include sub links for countries list)
-  Hospitality (Include sub links for hotels)
- Retail (Include sub links for attractions)
- Malls Group (Include sub links for malls)
- Technologies

 

2-      Department Homepage (Information technology for example but can be applied for Finance, HR, Marketing, Mall, Hotel…etc)

·         Department Announcements

·         Technology News

·         Project Office

·         Quick Links (Trelvix – Pendrum – IT Policies – Activity Calendar …)

·         Department Blog

·         Poll (Best Project – Employee of the month – Best Photography)... one poll  at time

 

Target Market(s)

real-estate employees

Industry/Entity Type

Real Estate

Requirements
Must have
• - Space in the corner for the logo (which is a square logo);
- Colors which match with navy blue & gold;
- Content centric design;
Should not have
• Scrolling - we want to try to limit the need for scrolling - especially on the portal home page.

```html
<!DOCTYPE html>
<html lang="en">
<head>
<meta charset="utf-8">
<title>The Real Estate — Group Portal</title>
<link rel="stylesheet" href="https://fonts.googleapis.com/css2?family=Arimo:wght@400;700&family=Cinzel:wght@700&family=Italianno&display=swap">
<style>
  :root {
    --sky-top: #b7bff5;
    --sky-mid: #c9cdf0;
    --sky-bottom: #d7d8df;
    --navy: #1c2a7c;
    --navy-deep: #14205f;
    --navy-text: #2c3a94;
    --gold: #f1d21c;
    --gold-soft: #e6c82a;
    --panel-top: #7b7b7b;
    --panel-bottom: #4e4e4e;
    --white: #ffffff;
    --ink: #1b1b1b;
    --ink-soft: #3a3a3a;
    --tile: #2e2e2e;
    --tile-text: #9a9a9a;
    --subtitle: #b9bccb;
  }
  * { box-sizing: border-box; margin: 0; padding: 0; }
  html, body { width: 1200px; height: 851px; overflow: hidden; }
  body {
    font-family: "Arimo", Arial, sans-serif;
    background: linear-gradient(180deg, var(--sky-top) 0%, var(--sky-mid) 45%, var(--sky-bottom) 100%);
    color: var(--ink);
  }
  .page { position: relative; width: 1200px; height: 851px; }
  .abs { position: absolute; }

  /* Header */
  .logo-box {
    left: 99px; top: 21px; width: 118px; height: 119px;
    background: linear-gradient(180deg, #22318c, var(--navy-deep));
    border: 4px solid var(--gold); border-radius: 9px;
    box-shadow: 3px 5px 8px rgba(0,0,0,.35);
    display: flex; align-items: flex-end; justify-content: center;
    color: var(--white); font-size: 17px; text-align: center; line-height: 1.35;
    padding-bottom: 12px;
  }
  .site-name {
    left: 234px; top: 26px; width: 140px;
    font-family: "Arimo", Arial, sans-serif; font-weight: 400;
    font-size: 32px; line-height: 36px; color: var(--navy-text);
  }
  .main-nav { left: 0; top: 44px; width: 1200px; height: 30px; list-style: none; }
  .main-nav li {
    position: absolute; top: 0;
    font-family: "Cinzel", serif; font-weight: 700; font-size: 14px; letter-spacing: .5px;
    color: var(--navy-text); text-shadow: 1px 1px 1px rgba(255,255,255,.6);
  }
  .main-nav li::after {
    content: ""; position: absolute; left: 50%; top: 20px; margin-left: -4px;
    border-left: 4px solid transparent; border-right: 4px solid transparent;
    border-top: 6px solid var(--gold-soft);
  }

  /* Hero */
  .hero-shadow {
    left: 56px; top: 424px; width: 1080px; height: 26px;
    background: radial-gradient(ellipse at center, rgba(0,0,0,.75) 0%, rgba(0,0,0,.35) 55%, rgba(0,0,0,0) 72%);
  }
  .hero {
    left: 409px; top: 113px; width: 704px; height: 324px; border-radius: 14px; overflow: hidden;
    background: radial-gradient(circle at 83% 6%, #3a4ab0 0%, #2a3a9e 30%, #1f2d86 55%, #1a2670 100%);
  }
  .hero-art {
    left: 94px; top: 8px; width: 282px; height: 316px;
    background: radial-gradient(ellipse at 50% 60%, rgba(200,215,245,.55) 0%, rgba(140,160,220,.3) 40%, rgba(40,55,140,0) 72%);
  }
  .hero-title {
    left: 293px; top: 36px; font-weight: 400;
    font-family: "Italianno", cursive; font-size: 78px; color: var(--gold); line-height: 1;
    text-shadow: 2px 2px 3px rgba(0,0,0,.4);
  }
  .hero-sub {
    left: 336px; top: 103px; font-size: 24px; color: var(--subtitle);
    text-shadow: 1px 1px 2px rgba(0,0,0,.5);
  }

  /* Side panels */
  .panel {
    background: linear-gradient(180deg, var(--panel-top), var(--panel-bottom));
    border-radius: 11px; color: var(--white);
    box-shadow: 0 6px 10px rgba(0,0,0,.35);
  }
  .panel-heading { color: var(--gold); font-size: 20px; font-weight: 400; text-shadow: 1px 1px 2px rgba(0,0,0,.6); }
  .quick-links { left: 93px; top: 161px; width: 267px; height: 276px; padding: 16px 10px 0 10px; }
  .quick-links .panel-heading { margin-bottom: 3px; }
  .link-item { font-size: 12.5px; line-height: 19px; letter-spacing: .2px; padding-bottom: 3px; border-bottom: 2px solid var(--gold-soft); margin-bottom: 9px; }
  .link-item .lead { color: var(--gold); }
  .read-more { color: var(--gold); float: right; }
  .link-item p::after, .announce::after { content: ""; display: block; clear: both; }

  .announcements { left: 93px; top: 469px; width: 267px; height: 282px; padding: 20px 10px 0 18px; }
  .announcements .panel-heading { margin-left: -3px; margin-bottom: 6px; }
  .announce { font-size: 13px; line-height: 15px; text-align: justify; padding: 0 0 6px 0; border-bottom: 2px solid var(--gold-soft); margin-bottom: 10px; }

  /* Centre column */
  .section-title { font-size: 19px; font-weight: 400; color: var(--ink); letter-spacing: .3px; }
  .press-image {
    left: 418px; top: 493px; width: 227px; height: 94px; border: 3px solid #3b3b3b;
    background: linear-gradient(180deg, #4f87d6 0%, #9cc2ef 55%, #6f8aa8 100%);
  }
  .press-text { left: 419px; top: 591px; width: 282px; font-size: 12.5px; line-height: 15px; text-align: justify; }
  .press-rule { left: 421px; top: 654px; width: 275px; height: 2px; background: var(--gold-soft); }
  .read-inline { color: var(--gold); float: right; }
  .tile {
    background: var(--tile); color: var(--tile-text); box-shadow: 2px 3px 5px rgba(0,0,0,.35);
    display: flex; align-items: center; justify-content: center;
  }
  .gallery-tile { top: 697px; width: 66px; height: 65px; font-size: 12px; padding-top: 14px; }

  /* Highlights */
  .highlights-text { left: 754px; top: 492px; width: 345px; font-size: 13px; line-height: 15px; text-align: justify; }
  .highlights-more { left: 1017px; top: 561px; font-size: 13px; color: var(--gold); }
  .feature-tile { top: 585px; width: 112px; height: 89px; font-size: 18px; }
  .feature-caption { top: 686px; width: 110px; font-size: 11px; line-height: 11.5px; text-align: justify; color: var(--ink-soft); }
  .feature-more { top: 763px; width: 104px; text-align: right; font-size: 11px; color: var(--gold); letter-spacing: .5px; }

  /* Footer */
  .footer-links { left: 0; top: 790px; width: 1200px; text-align: center; font-size: 12px; list-style: none; letter-spacing: .3px; }
  .footer-links li { display: inline-block; padding: 0 6px; border-left: 2px solid var(--gold-soft); line-height: 14px; }
  .footer-links li:first-child { border-left: 0; }
  .copyright { left: 0; top: 815px; width: 1200px; text-align: center; font-size: 11px; letter-spacing: .6px; margin-left: -10px; }
</style>
</head>
<body>
<div class="page">

  <header>
    <div class="abs logo-box">Company<br>Logo</div>
    <div class="abs site-name">The<br>Real<br>Estate</div>
    <ul class="abs main-nav">
      <li style="left:404px">Properties</li>
      <li style="left:528px">International</li>
      <li style="left:688px">Hospitality</li>
      <li style="left:823px">Retail</li>
      <li style="left:913px">Malls</li>
      <li style="left:995px">Technologies</li>
    </ul>
  </header>

  <div class="abs hero-shadow"></div>
  <section class="abs hero">
    <div class="abs hero-art" role="img" aria-label="Photograph of a tall glass skyscraper rising into a blue sky"></div>
    <h1 class="abs hero-title">The real Estate</h1>
    <p class="abs hero-sub">Lorem ipsum dolor sit amet</p>
  </section>

  <aside class="abs panel quick-links">
    <h2 class="panel-heading">Quick Links</h2>
    <div class="link-item"><div class="lead">Lorem ipsum dolor sit amet, consectetur</div><p>Lorem ipsum dolor sit amet, consectetur adipiscing elit. <span class="read-more">Read More...</span></p></div>
    <div class="link-item"><div class="lead">Lorem ipsum dolor sit amet, consectetur</div><p>Lorem ipsum dolor sit amet, consectetur adipiscing elit. <span class="read-more">Read More...</span></p></div>
    <div class="link-item"><div class="lead">Lorem ipsum dolor sit amet, consectetur</div><p>Lorem ipsum dolor sit amet, consectetur adipiscing elit. <span class="read-more">Read More...</span></p></div>
  </aside>

  <aside class="abs panel announcements">
    <h2 class="panel-heading">Company Announcements</h2>
    <p class="announce">Lorem ipsum dolor sit amet, consectetur adipiscing elit. Duis fringilla arcu erat, eget hendrerit neque. In pretium interdum dolor, lobortis molestie libero euismod nec. Maecenas malesuada tempus magna a <span class="read-more">Read More...</span></p>
    <p class="announce">Lorem ipsum dolor sit amet, consectetur adipiscing elit. Duis fringilla arcu erat, eget hendrerit neque. In pretium interdum dolor, lobortis molestie libero euismod nec. Maecenas malesuada tempus magna a <span class="read-more">Read More...</span></p>
  </aside>

  <section>
    <h2 class="abs section-title" style="left:418px;top:466px">Qalvor in Press</h2>
    <div class="abs press-image" role="img" aria-label="Photograph of a blank billboard above a city skyline"></div>
    <p class="abs press-text">Lorem ipsum dolor sit amet, consectetur adipiscing elit. Duis fringilla arcu erat, eget hendrerit neque. In pretium inter-dumdolor, <span class="read-inline">Read More...</span></p>
    <div class="abs press-rule"></div>
  </section>

  <section>
    <h2 class="abs section-title" style="left:421px;top:669px">Photo Gallery</h2>
    <div class="abs tile gallery-tile" style="left:414px">Image</div>
    <div class="abs tile gallery-tile" style="left:488px">Image</div>
    <div class="abs tile gallery-tile" style="left:559px">Image</div>
    <div class="abs tile gallery-tile" style="left:631px">Image</div>
  </section>

  <section>
    <h2 class="abs section-title" style="left:754px;top:466px;color:var(--ink-soft)">Highlights &amp; Achievements</h2>
    <p class="abs highlights-text">Lorem ipsum dolor sit amet, consectetur adipiscing elit. Duis fringilla arcu erat, eget hendrerit neque. In pretium interdum dolor, lobortis molestie libero euismod nec. Maecenas malesuada tempus magna a laoreet. Sedid.</p>
    <span class="abs highlights-more">Read More...</span>

    <div class="abs tile feature-tile" style="left:751px">Image</div>
    <div class="abs tile feature-tile" style="left:874px">Image</div>
    <div class="abs tile feature-tile" style="left:1000px">Image</div>

    <p class="abs feature-caption" style="left:751px">Lorem ipsum dolor sit amet, consectetur adipiscing elit. Duis fringilla arcu erat, eget hendrerit neque. In prtium intedum</p>
    <p class="abs feature-caption" style="left:874px">Lorem ipsum dolor sit amet, consectetur adipiscing elit. Duis fringilla arcu erat, eget hendrerit neque. In prtium intedum</p>
    <p class="abs feature-caption" style="left:1000px">Lorem ipsum dolor sit amet, consectetur adipiscing elit. Duis fringilla arcu erat, eget hendrerit neque. In prtium intedum</p>

    <span class="abs feature-more" style="left:751px">read more...</span>
    <span class="abs feature-more" style="left:874px">read more...</span>
    <span class="abs feature-more" style="left:1000px">read more...</span>
  </section>

  <footer>
    <ul class="abs footer-links">
      <li>Blog</li><li>Support</li><li>Solutions</li><li>Testimonials</li><li>Developments</li><li>Projects</li><li>Contact Us</li>
    </ul>
    <p class="abs copyright">© 2012 Your Company. All Rights Reserved</p>
  </footer>

</div>
</body>
</html>
```